Glofarvik - Start-up company selling electricity

Hello let me tell you about Glofarvik.

Glofarvik is start-up company selling electricity in Iceland. The operations of the company consist of making power usage forecasts for our customers, purchasing the electricity wholesale from the energy producers, and selling the electricity to the consumer. We are focused on tech by using optimization and machine learning to minimize electricity prices to our customers. Our marketing strategy is to portray a tech company mindset and to show dedication to driving down the electricity price on the market.

We need your help to make our website pop. Possible concepts to work with are as follows:

- Iceland the land of ice and fire
- Green energy
- Innovation
- Tech and data science

Link to our website: https://prufa.glofarvik-example.is/
We are open to ideas.
Thank you!

Target Market(s)

Electricity consumers both homes and companies.

Number of Pages Required

1 page

Font styles to use
Serif
Sans Serif

```html
<!DOCTYPE html>
<html lang="en">
<head>
<meta charset="utf-8">
<title>Glofarvik – Same electricity, just cheaper</title>
<link href="https://fonts.googleapis.com/css2?family=Lustria&family=Arimo:wght@400&display=swap" rel="stylesheet">
<style>
:root{
  --navy:#13224a;
  --red:#8e2022;
  --red-dark:#7a1a1c;
  --white:#ffffff;
  --text:#3a3a3a;
  --serif:'Lustria', Georgia, serif;
  --sans:'Arimo', Arial, sans-serif;
}
*{margin:0;padding:0;box-sizing:border-box}
html,body{width:1200px;height:2607px;overflow:hidden;background:var(--white)}
body{position:relative;font-family:var(--serif);color:var(--navy)}
.abs{position:absolute}
.site-header{top:0;left:0;width:1200px;height:128px}
.brand{left:112px;top:40px;display:flex;align-items:center;gap:12px;font-size:40px;color:var(--red);letter-spacing:0.5px}
.brand-dot{width:34px;height:34px;border-radius:50%;background:var(--navy)}
.main-nav{right:112px;top:56px;display:flex;gap:51px;font-size:18px;color:#333}
.hero{top:128px;left:0;width:1200px;height:720px}
.hero-title{top:252px;left:0;width:1200px;text-align:center;color:var(--white);font-size:92px;letter-spacing:1px;line-height:1}
.hero-sub{top:355px;left:0;width:1200px;text-align:center;color:var(--white);font-size:32px}
.section-title{font-size:40px;line-height:1;font-weight:400}
.rule{height:3px;width:52px;background:var(--navy)}
.welcome-title{left:156px;top:950px}
.welcome-title span{color:var(--red)}
.welcome-rule{left:156px;top:1006px}
.welcome-text{left:156px;top:1030px;width:515px;font-family:var(--sans);font-size:14.5px;line-height:27.5px;color:var(--text);text-align:justify}
.btn{display:flex;align-items:center;justify-content:center;color:var(--white);font-family:var(--serif);border-radius:3px;font-size:17px}
.btn-red{background:var(--red)}
.btn-navy{background:var(--navy)}
.btn-company{left:156px;top:1250px;width:146px;height:52px}
.btn-home{left:310px;top:1250px;width:146px;height:52px}
.welcome-visual{left:775px;top:1000px;width:270px;height:270px;border-radius:50%;background:linear-gradient(160deg,#a63a3c 0%,#5a4a6a 50%,#2c4472 100%)}
.price-band{top:1385px;left:0;width:1200px;height:520px}
.price-title{top:1445px;left:0;width:1200px;text-align:center;color:var(--white)}
.price-rule{left:574px;top:1500px;background:var(--white)}
.price-divider{left:600px;top:1545px;width:1px;height:152px;background:rgba(255,255,255,.3)}
.price{width:300px;text-align:center;color:var(--white)}
.price-num{font-size:74px;line-height:1}
.price-unit{font-size:24px;margin-top:14px}
.price-a{left:212px;top:1560px}
.price-b{left:675px;top:1560px}
.price-note{top:1726px;left:0;width:1200px;text-align:center;color:var(--white);font-size:22px}
.btn-compare{left:501px;top:1783px;width:199px;height:52px;font-size:18px}
.future-title{top:1975px;left:0;width:1200px;text-align:center}
.future-rule{left:574px;top:2032px}
.future-text{top:2062px;left:225px;width:750px;text-align:center;font-family:var(--sans);font-size:14px;line-height:30px;color:var(--text)}
.btn-more{left:517px;top:2205px;width:165px;height:52px;font-size:19px}
.footer-bg{top:2210px;left:0;width:1200px;height:397px}
.footer-brand{left:143px;top:2420px;display:flex;align-items:center;gap:14px;font-size:40px;color:var(--white)}
.footer-brand .brand-dot{background:var(--white)}
.footer-col{top:2388px;font-size:17px;line-height:37px;color:var(--white)}
.footer-col-a{left:534px}
.footer-col-b{left:826px}
.footer-line{left:112px;top:2523px;width:976px;height:1px;background:rgba(255,255,255,.12)}
.copyright{top:2550px;left:0;width:1200px;text-align:center;color:var(--white);font-size:15px}
</style>
</head>
<body>
<header class="site-header abs">
  <div class="brand abs"><span class="brand-dot"></span>GLOFARVIK</div>
  <nav class="main-nav abs"><span>Terms of business</span><span>Question &amp; Answer</span><span>About Glofarvik</span></nav>
</header>

<section class="hero abs">
  <svg width="1200" height="720" viewBox="0 0 1200 720" class="abs" style="left:0;top:0">
    <defs>
      <linearGradient id="heroSky" x1="0" y1="0" x2="0" y2="1">
        <stop offset="0" stop-color="#5a3a4a"/>
        <stop offset="0.35" stop-color="#6e4552"/>
        <stop offset="0.6" stop-color="#3c4258"/>
        <stop offset="1" stop-color="#4d5766"/>
      </linearGradient>
    </defs>
    <path d="M0 585 Q600 831 1200 585 V585 L1200 0 H0 Z" fill="var(--red)"/>
    <path d="M0 0 H1200 V585 Q600 792 0 585 Z" fill="url(#heroSky)" role="img" aria-label="Icelandic waterfalls under a dramatic cloudy sky"/>
  </svg>
  <h1 class="hero-title abs" style="font-weight:400">GLOFARVIK</h1>
  <p class="hero-sub abs">Same electricity ~ just cheaper!</p>
</section>

<h2 class="section-title welcome-title abs">Welcome to <span>Glofarvik</span></h2>
<div class="rule welcome-rule abs"></div>
<p class="welcome-text abs">Sed ut perspiciatis unde omnis iste natus error sit voluptatem accusant ium dolor emque laudantium, totam rem aperiam, eaque ipsa quae ab illo inventore veritat is et quasi architecto beatae vitae dicta sunt explicabo. Nemo enim ipsam volupt atem quia voluptas sit aspernatur aut odit aut fugit, sed quia consequuntur magni dolores eos qui ratione voluptatem sequi nesciunt.Neque porro quisquam est, qui dolorem ipsum quia dolor sit amet, consectetur, adipisci velit, sed quia non ut labore et dolore magnam aliquam quaerat voluptatem.</p>
<a class="btn btn-red btn-company abs">COMPANY</a>
<a class="btn btn-navy btn-home abs">HOME</a>
<div class="welcome-visual abs" role="img" aria-label="Icelandic landscape in red and blue tones"></div>

<svg class="price-band abs" width="1200" height="520" viewBox="0 0 1200 520" role="img" aria-label="Red toned landscape background">
  <defs>
    <linearGradient id="priceFill" x1="0" y1="0" x2="1" y2="1">
      <stop offset="0" stop-color="#8c2124"/>
      <stop offset="1" stop-color="#93262a"/>
    </linearGradient>
  </defs>
  <path d="M0 55 Q600 -45 1200 55 V445 Q600 585 0 445 Z" fill="url(#priceFill)"/>
</svg>
<h2 class="section-title price-title abs">Price List</h2>
<div class="rule price-rule abs"></div>
<div class="price-divider abs"></div>
<div class="price price-a abs"><div class="price-num">6.95</div><div class="price-unit">ISK / kWh</div></div>
<div class="price price-b abs"><div class="price-num">6.22</div><div class="price-unit">ISK / kWh</div></div>
<p class="price-note abs">Electric Acceleration Make a price comparison</p>
<a class="btn btn-navy btn-compare abs">Verdvaki</a>

<h2 class="section-title future-title abs">The Future is Exciting</h2>
<div class="rule future-rule abs"></div>
<p class="future-text abs">Let's make the electricity system smarter together. Glofarvik uses artificial intelligence, data science and automation to minimize costs and promote eccentricity Neque porro quisquam est, qui dolorem ipsum quia dolor sit amet, consectetur eius modi tempora incidunt ut labore et dolore magnam aliquam quaerat voluptatem. Ut enim ad minima veniam, quis nos xercitationem ullam corporis suscipit laboriosam, nisi ut aliquid ex ea commodi consequatur</p>
<a class="btn btn-red btn-more abs">Read More</a>

<svg class="footer-bg abs" width="1200" height="397" viewBox="0 0 1200 397">
  <path d="M0 12 Q600 235 1200 12 V397 H0 Z" fill="var(--navy)"/>
</svg>
<footer>
  <div class="footer-brand abs"><span class="brand-dot"></span>GLOFARVIK</div>
  <div class="footer-col footer-col-a abs">Glofarvik ehf<br>ID number: 123456-7890<br>VAT number: 204817</div>
  <div class="footer-col footer-col-b abs">Ljósvegur 7, 101 Reykjavík<br>hallo@glofarvik-example.is<br>555-0142</div>
  <div class="footer-line abs"></div>
  <p class="copyright abs">© Copyright 2021 Glofarvik.All rights reserved.</p>
</footer>
</body>
</html>
```